Stationery design for law/Property/finance business

We need stationery design for a Law/Property/Finance business called Ridgemoor. Logo is attached.
we require a letterhead and with compliments slip.
Would like to see a very simple professional design using the colours of the logo and offset against Charcoal colours. Maybe a charcoal band for header and footer with logo and details appearing in it? Former letterhead attached for examples.
we require the project to be provided in word, pdf and jpeg format.
we require the following details on the stationery:
Cairns Phone: 07 40551926
Weipa Phone: 07 40613847
Mobile: 0491 570 384
Fax: 07 40338172
email: admin@ridgemoorholdings-example.com.au
ABN 51 824 306 917

```html
<!DOCTYPE html>
<html lang="en">
<head>
<meta charset="utf-8">
<title>Ridgemoor Stationery</title>
<link rel="stylesheet" href="https://fonts.googleapis.com/css2?family=Montserrat:wght@400;600&family=Short+Stack&display=swap">
<style>
  :root {
    --backdrop: #b8b8b8;
    --paper: #ffffff;
    --charcoal: #212121;
    --brand-blue: #1f8fd8;
    --accent-cyan: #3bb6e8;
    --footer-text: #e6e6e6;
  }
  * { box-sizing: border-box; margin: 0; padding: 0; }
  html, body { width: 1200px; height: 1200px; overflow: hidden; }
  body {
    background: var(--backdrop);
    font-family: "Montserrat", Arial, sans-serif;
    position: relative;
  }
  .sheet { position: absolute; background: var(--paper); overflow: hidden; }
  .band {
    position: absolute; left: 0; right: 0;
    background: var(--charcoal);
    display: flex; align-items: center;
  }
  .wordmark {
    font-family: "Montserrat", Arial, sans-serif;
    font-weight: 600;
    color: var(--brand-blue);
    letter-spacing: 0.5px;
    text-transform: uppercase;
  }
  .contact {
    color: var(--footer-text);
    font-size: 7.5px;
    line-height: 10.5px;
    display: flex; align-items: center; gap: 3px;
    white-space: nowrap;
  }
  .contact svg { width: 7px; height: 7px; fill: var(--footer-text); flex: none; }

  /* Letterhead */
  .letterhead { left: 334px; top: 79px; width: 517px; height: 732px; }
  .letterhead .header { top: 17px; height: 66px; justify-content: center; }
  .letterhead .wordmark { font-size: 20px; }
  .letterhead .footer { top: 697px; height: 26px; }
  .footer-col { position: absolute; top: 3px; }
  .footer-col.phones { left: 44px; }
  .footer-col.lines { left: 196px; }
  .footer-col.office { left: 318px; }

  /* Compliments slip */
  .comp-slip { left: 293px; top: 848px; width: 614px; height: 288px; }
  .comp-slip .header { top: 13px; height: 51px; justify-content: space-between; padding: 0 42px 0 52px; }
  .comp-slip .wordmark { font-size: 16px; }
  .comp-title {
    font-family: "Short Stack", "Comic Sans MS", cursive;
    color: var(--accent-cyan);
    font-size: 15px;
  }
  .comp-slip .footer { top: 260px; height: 20px; justify-content: center; gap: 22px; padding-left: 12px; }
  .comp-slip .contact { font-size: 9.5px; }
  .comp-slip .contact svg { width: 8px; height: 8px; }
</style>
</head>
<body>

<svg width="0" height="0" style="position:absolute">
  <defs>
    <symbol id="icon-phone" viewBox="0 0 10 10"><path d="M1 3.5 Q5 0.5 9 3.5 L8 5 L6.5 4.2 L6.5 3.4 Q5 3 3.5 3.4 L3.5 4.2 L2 5 Z M2.5 5.5 H7.5 L8.5 9 H1.5 Z"/></symbol>
    <symbol id="icon-mobile" viewBox="0 0 10 10"><path d="M3 0.5 H7 V9.5 H3 Z M3.8 1.5 V7.5 H6.2 V1.5 Z"/></symbol>
    <symbol id="icon-fax" viewBox="0 0 10 10"><path d="M3 0.5 H7 V4 H3 Z M1 4 H9 V9.5 H1 Z"/></symbol>
    <symbol id="icon-mail" viewBox="0 0 10 10"><path d="M1 4 L5 1 L9 4 V9.5 H1 Z M2 4.5 L5 7 L8 4.5 Z"/></symbol>
  </defs>
</svg>

<section class="sheet letterhead" aria-label="Letterhead">
  <header class="band header">
    <span class="wordmark">Ridgemoor</span>
  </header>
  <footer class="band footer">
    <div class="footer-col phones">
      <p class="contact"><svg><use href="#icon-phone"/></svg>07 40551926&nbsp; (Cairns)</p>
      <p class="contact"><svg><use href="#icon-phone"/></svg>07 40613847&nbsp; (Weipa)</p>
    </div>
    <div class="footer-col lines">
      <p class="contact"><svg><use href="#icon-mobile"/></svg>0491 570 384</p>
      <p class="contact"><svg><use href="#icon-fax"/></svg>07 40338172</p>
    </div>
    <div class="footer-col office">
      <p class="contact"><svg><use href="#icon-mail"/></svg>admin@ridgemoorholdings-example.com.au</p>
      <p class="contact">ABN 51 824 306 917</p>
    </div>
  </footer>
</section>

<section class="sheet comp-slip" aria-label="With compliments slip">
  <header class="band header">
    <span class="wordmark">Ridgemoor</span>
    <span class="comp-title">With Compliments</span>
  </header>
  <footer class="band footer">
    <p class="contact"><svg><use href="#icon-mobile"/></svg>0491 570 384</p>
    <p class="contact"><svg><use href="#icon-fax"/></svg>07 40338172</p>
    <p class="contact"><svg><use href="#icon-phone"/></svg>07 40551926&nbsp; (Cairns)</p>
    <p class="contact"><svg><use href="#icon-phone"/></svg>07 40613847&nbsp; (Weipa)</p>
  </footer>
</section>

</body>
</html>
```